Enamel Pride Season infographic - Every Chapter Counts Here

To create an infographic for Enamel Pride Season, August 2014, with the key messages of how the health of your mouth affects you through your lifetime.
We require two posters (A3 and A4 options) that will educate the Australian and New Zealand public of the importance of maintaining good oral health through facts and statistics (see attachments), focusing on different stages in your life.
The A3 poster will be used for: hanging in dental practices, posted in social media, on websites, advertising, public relations.
The A4 poster will be used for print handouts, websites, advertising, public relations.
Sections of the posters will be pulled out to be used in social media posts, on websites, in emails, etc.
Design constraints:
Poster One: Infographic Poster to be A3 (Appendix 1)
Poster Two: Infographic Poster to be reconfigured as A4 handout with limited facts (Appendix 2).
Full colour with the RGV colour palette reflected throughout.
Deliverables:
Design two infographics to reflect the tagline, Every Chapter Counts Here, and:
• One A3 poster to represents the key milestones as outlined in Appendix 1.
One A4 poster/handout to represent the key milestones in Appendix 2.
• Is obvious that these are stages in your life but does not mention the specific ages.
• Facts can be represented in icons, images, graphs, fractions, percentages, etc.
• Can be broken into smaller campaign sub messages.
• Includes: Enamel Pride Season and Every Chapter Counts Here text.
• Includes: A RGV Initiative logo.
• Includes August 2014 as Enamel Pride Season.
• Include website: www.dentalridgevale.com
• Is similar in style to the RGV launch infographic (attached).
• Clean, vibrant, understandable and friendly.
Tone:
RGV is experienced, reliable, caring, accessible, knowledgeable, friendly and confident in all aspects of dentistry.
The infographic can be ‘Tongue in cheek’ – friendly tone to suit different age groups through the messages, ie. 18-25 years is more conversational and cheeky, while 50+ could come from a ‘dad joke.’
See attached logo, colour palette and appendices.
Aussie and Kiwi families visiting a modern, bright, well-presented dental practice.
- Bright, clear and engaging. Needs to be suited to a professional dental practice, but also stand out on social media and in advertising.
Must have name of campaign and month, brand supporter, website - see brief.

```html
<!DOCTYPE html>
<html lang="en">
<head>
<meta charset="utf-8">
<title>Enamel Pride Season – Every Chapter Counts Here</title>
<link href="https://fonts.googleapis.com/css2?family=Montserrat:wght@300;400;700&family=Open+Sans:wght@400;700;800&display=swap" rel="stylesheet">
<style>
  :root{
    --sky:#0a99dc;
    --sun:#f2bb00;
    --earth:#5d5249;
    --earth-shade:#3a322d;
    --navy:#1f5489;
    --crowd:#1f5b8f;
    --crowd-soft:#2a6aa0;
    --white:#ffffff;
  }
  *{margin:0;padding:0;box-sizing:border-box}
  html,body{width:849px;height:1200px;overflow:hidden;background:var(--sky)}
  .poster{position:relative;width:849px;height:1200px;background:var(--sky);color:var(--white);font-family:"Open Sans",Arial,sans-serif;overflow:hidden}
  .masthead{position:absolute;left:0;top:0;width:849px;height:194px;background:var(--sun);text-align:center;font-family:"Montserrat",Arial,sans-serif;padding-top:50px}
  .masthead-title{font-weight:700;font-size:31px;letter-spacing:1px;line-height:38px;text-transform:uppercase}
  .masthead-tagline{font-weight:300;font-size:33px;letter-spacing:1.5px;line-height:40px;text-transform:uppercase}
  .masthead-date{font-weight:400;font-size:15px;letter-spacing:3px;line-height:22px;margin-top:8px;text-transform:uppercase}
  .masthead-rule{position:absolute;left:0;top:194px;width:849px;height:9px;background:var(--earth)}
  .family-area{position:absolute;left:225px;top:640px;width:565px;height:470px;border-radius:120px 120px 0 0;background:linear-gradient(180deg,var(--crowd-soft),var(--crowd))}
  .artwork{position:absolute;left:0;top:0}
  .stat-figure{position:absolute;font-family:"Montserrat",Arial,sans-serif;font-weight:700;font-size:50px;line-height:1;letter-spacing:1px}
  .stat-text{position:absolute;font-size:17px;line-height:23px}
  .fact{position:absolute;font-size:15px;line-height:19px}
  .fact h3{font-family:"Open Sans",Arial,sans-serif;font-weight:800;font-size:15px;letter-spacing:.3px;text-transform:uppercase}
  .fact b{font-weight:800}
  .fact--right{text-align:right}
  .fact--center{text-align:center}
  .donut-label{position:absolute;left:188px;top:722px;width:84px;text-align:center;font-family:"Montserrat",Arial,sans-serif;font-weight:700;font-size:30px}
  .coin-sign{position:absolute;width:80px;text-align:center;font-family:"Montserrat",Arial,sans-serif;font-weight:700;font-size:58px;line-height:1}
  .brand{position:absolute;left:70px;top:1010px;font-family:"Open Sans",Arial,sans-serif}
  .brand-name{font-weight:800;font-size:86px;line-height:90px;letter-spacing:2px}
  .brand-sub{font-weight:400;font-size:27px;line-height:30px;margin-top:6px}
  .site{position:absolute;right:60px;top:1124px;font-size:19px}
</style>
</head>
<body>
<div class="poster">
  <header class="masthead">
    <h1 class="masthead-title">Enamel Pride Season a RGV Initiative</h1>
    <p class="masthead-tagline">Every Chapter Counts Here</p>
    <p class="masthead-date">August 2014</p>
  </header>
  <div class="masthead-rule"></div>

  <div class="family-area" role="img" aria-label="Silhouettes of a family of several generations standing together"></div>

  <svg class="artwork" width="849" height="1200" viewBox="0 0 849 1200">
    <g class="ribbon">
      <rect x="356" y="296" width="74" height="31" fill="var(--earth)"/>
      <polygon points="356,296 430,296 356,327" fill="var(--earth-shade)"/>
      <rect x="0" y="238" width="405" height="58" fill="var(--earth)"/>
      <polygon points="461,270 849,270 849,327 430,327 430,298" fill="var(--navy)"/>
    </g>
    <g class="ribbon">
      <rect x="356" y="418" width="74" height="32" fill="var(--earth)"/>
      <polygon points="356,418 430,418 356,450" fill="var(--earth-shade)"/>
      <rect x="0" y="360" width="405" height="58" fill="var(--earth)"/>
      <polygon points="461,393 849,393 849,450 430,450 430,421" fill="var(--navy)"/>
    </g>
    <circle cx="368" cy="563" r="53" fill="none" stroke="var(--sun)" stroke-width="17"/>
    <circle cx="368" cy="563" r="44" fill="var(--sky)"/>
    <circle cx="681" cy="621" r="53" fill="none" stroke="var(--sun)" stroke-width="17"/>
    <circle cx="681" cy="621" r="44" fill="var(--sky)"/>
    <circle cx="230" cy="741" r="56" fill="none" stroke="var(--navy)" stroke-width="22"/>
    <path d="M269.6,701.4 A56,56 0 1,0 230,797" fill="none" stroke="var(--sun)" stroke-width="22"/>
    <circle cx="230" cy="741" r="45" fill="var(--sky)"/>
    <g stroke="var(--white)" stroke-width="2" fill="none">
      <line x1="368" y1="628" x2="368" y2="690"/>
      <line x1="681" y1="686" x2="681" y2="750"/>
      <line x1="596" y1="718" x2="596" y2="782"/>
      <polyline points="230,820 230,882 264,882"/>
    </g>
    <g fill="var(--white)">
      <circle cx="368" cy="692" r="5"/>
      <circle cx="681" cy="751" r="5"/>
      <circle cx="596" cy="718" r="5"/>
      <circle cx="265" cy="882" r="5"/>
    </g>
  </svg>

  <div class="stat-figure" style="left:265px;top:246px">90%</div>
  <p class="stat-text" style="left:466px;top:286px">of all dental disease is preventable</p>
  <div class="stat-figure" style="left:265px;top:368px">48%</div>
  <p class="stat-text" style="left:466px;top:398px">people remember a smile on first<br>impression than anything else</p>

  <div class="coin-sign" style="left:328px;top:534px">$</div>
  <div class="coin-sign" style="left:641px;top:592px">$</div>
  <div class="donut-label">50%</div>

  <div class="fact fact--right" style="right:552px;top:523px">
    <h3>Like pulling teeth!</h3>
    <p>Busy parents <b>600,000</b><br>days lost from school</p>
  </div>
  <div class="fact fact--right" style="right:552px;top:608px">
    <h3>Watch your mouth!</h3>
    <p>Young adults haven't visited<br>a dentist within past 12 months</p>
  </div>
  <div class="fact fact--right" style="right:100px;top:478px">
    <h3>Working on it!</h3>
    <p><b>1 MILLION</b> working adults lost days<br>of work each year</p>
  </div>
  <div class="fact fact--center" style="left:290px;top:793px;width:420px">
    <h3>A gateway to health!</h3>
    <p>Grandparents More than 90 percent of<br>all systemic diseases — including heart disease —<br>have oral symptoms</p>
  </div>

  <div class="brand">
    <div class="brand-name">RGV</div>
    <div class="brand-sub">dental ridgevale</div>
  </div>
  <div class="site">dentalridgevale.com.au</div>
</div>
</body>
</html>
```